Healthy Snack Bar Wrapper Design

We are passionate about delivering healthy and tasty treats that are Raw, Organic, Preservative Free, Gluten Free, have No Added Sugar and No Additives!
In this project we are looking for a design for a new healthy food product to be launched soon in Australia. The packaging will be a bar wrapper made from foil that will be hot sealed, with a front and a back.
The snack is a raw, organic and healthy treat made predominantly with nuts, and will come in 3 initial flavours:
- Black Forest (Sour Cherry and Choc)
- Plum Fandango (Banana, Apricot and Blueberry)
- Zestivelle (Pineapple, Passionfruit and Kiwi)
The product name is NibbleMoss, which does not currently have a logo. We are happy to have this as a simple written component of the initial design at the top of the packaging, perhaps within an circle, square or oval.
The typeface used for the names and the main ingredients should be fun.
The overall design should be very simple and make use of minimal colours. Our preferences are to have a plain colour for the background, such as light organic brown or white, with an eye catching colour that can be used to define the flavour, but should not be too vibrant.
We do not want to have an 3 dimensional images or objects. Nor do we want to have product images and any imagery should be only to give the impression of the flavours within rather than an image of the flavour. Finally, we do not want to have gradients included in the design.
The final design should communicate healthy, tasty and fun!
Examples of inspiration designs are attached in the files.
Main Information:
- The front should comprise of the following information:
-- NibbleMoss
-- Flavour name (such as Black Forest)
-- Main Ingredients (Sour Cherry and Choc) (This is optional)
-- Portion size (60g)
-- Message (This is optional)
--- 0% Additives
--- 60% Nuts
--- 100% Natural
- The back needs to have space for the following information:
-- Nutritional Information
-- Barcode
-- Ingredients
-- Contact information
- Wrapper Dimensions
-- Width: 14cm
-- Height: 15cm
- Bar Dimensions
-- Width: 3cm
-- Height: 10cm
-- Depth: 2.5cm
Target Market(s)
People who want to have a healthy tasty treat
Colors
Designer to choose colors to be used in the design.
Requirements
Must have
- Main Information:
- - The front should comprise of the following information:
- -- NibbleMoss
- -- Flavour name (such as Black Forest)
- -- Main Ingredients (Sour Cherry and Choc) (This is optional)
- -- Portion size (60g)
- -- Message (This is optional)
- --- 0% Additives
- --- 60% Nuts
- --- 100% Natural
- - The back needs to have space for the following information:
- -- Nutritional Information
- -- Barcode
- -- Ingredients
- -- Contact information
- - Wrapper Dimensions
- -- Width: 14cm
- -- Height: 15cm
- - Bar Dimensions
- -- Width: 3cm
- -- Height: 10cm
- -- Depth: 2.5cm
Should not have
- We do not want to have an 3 dimensional images or objects. Nor do we want to have product images and any imagery should be only to give the impression of the flavours within rather than an image of the flavour. Finally, we do not want to have gradients included in the design.

```html
<!DOCTYPE html>
<html lang="en">
<head>
<meta charset="utf-8">
<title>NibbleMoss Bar Wrappers</title>
<link rel="stylesheet" href="https://fonts.googleapis.com/css2?family=Patrick+Hand&family=Gaegu&family=Open+Sans:wght@400&display=swap">
<style>
  :root {
    --page: #ffffff;
    --brand-red: #e0141b;
    --badge-green: #2fb52a;
    --leaf: #9ccf3a;
    --ink: #111111;
    --white: #ffffff;
    --forest: #4a2410;
    --forest-dots: #8a5a3a;
    --forest-accent: #e3c11d;
    --plum: #f39316;
    --plum-dots: #f8c534;
    --plum-accent: #7a3d0d;
    --zest: #f2bd16;
    --zest-dots: #ee9d1e;
    --zest-accent: #6e4708;
  }
  * { box-sizing: border-box; margin: 0; padding: 0; }
  html, body { width: 1101px; height: 1200px; overflow: hidden; background: var(--page); }
  .canvas { position: relative; width: 1101px; height: 1200px; }

  .wrapper {
    position: absolute; left: 25px; width: 1052px; height: 356px;
    background: var(--wrap); overflow: hidden;
  }
  .wrapper--forest { top: 20px;  --wrap: var(--forest); --dots: var(--forest-dots); --accent: var(--forest-accent); --weight-colour: var(--white);     --name-left: 455px; --name-size: 92px; --ing-left: 455px; }
  .wrapper--plum   { top: 419px; --wrap: var(--plum);   --dots: var(--plum-dots);   --accent: var(--plum-accent);   --weight-colour: var(--plum-dots); --name-left: 427px; --name-size: 88px; --ing-left: 438px; }
  .wrapper--zest   { top: 832px; --wrap: var(--zest);   --dots: var(--zest-dots);   --accent: var(--zest-accent);   --weight-colour: var(--zest-dots); --name-left: 455px; --name-size: 92px; --ing-left: 446px; }

  .seal {
    position: absolute; top: 0; bottom: 0; width: 38px;
    background: repeating-linear-gradient(90deg, rgba(0,0,0,0.12) 0 2px, transparent 2px 7px);
  }
  .seal--left { left: 0; }
  .seal--right { right: 0; }

  .flavour-texture {
    position: absolute; left: 640px; top: 30px; width: 380px; height: 310px;
    border-radius: 50%; background: var(--dots); opacity: 0.35;
  }

  .brand-tag {
    position: absolute; left: 171px; top: 35px; width: 167px; height: 114px;
    background: var(--brand-red); display: flex; align-items: flex-end; justify-content: center;
    padding-bottom: 18px;
  }
  .brand-name {
    font-family: "Open Sans", sans-serif; font-size: 24px; color: var(--white); letter-spacing: -0.3px;
    white-space: nowrap;
  }

  .claims { position: absolute; left: 135px; top: 140px; width: 284px; height: 154px; }
  .claims svg { position: absolute; inset: 0; }
  .claims-leaf { position: absolute; left: 14px; top: 58px; width: 66px; height: 76px; border-radius: 50% 0 50% 0; background: var(--leaf); }
  .claims-list {
    position: absolute; right: 36px; top: 40px; list-style: none; text-align: right;
    font-family: "Open Sans", sans-serif; font-size: 21px; line-height: 32px; color: var(--white);
    white-space: nowrap;
  }

  .flavour-name {
    position: absolute; left: var(--name-left); top: 118px;
    font-family: "Patrick Hand", cursive; font-weight: 400; font-size: var(--name-size); line-height: 1;
    text-transform: uppercase; white-space: nowrap;
    color: var(--white); -webkit-text-stroke: 8px var(--ink); paint-order: stroke fill;
    letter-spacing: 0;
  }
  .ingredients {
    position: absolute; left: var(--ing-left); top: 236px;
    font-family: "Gaegu", cursive; font-size: 36px; line-height: 1; color: var(--accent);
    white-space: nowrap;
  }
  .portion {
    position: absolute; right: 92px; top: 290px;
    font-family: "Open Sans", sans-serif; font-size: 21px; line-height: 1; color: var(--weight-colour);
    white-space: nowrap;
  }
</style>
</head>
<body>
<main class="canvas">

  <section class="wrapper wrapper--forest">
    <div class="seal seal--left"></div><div class="seal seal--right"></div>
    <div class="flavour-texture" role="img" aria-label="Soft dotted pattern hinting at the flavour"></div>
    <div class="brand-tag"><span class="brand-name">NibbleMoss</span></div>
    <div class="claims">
      <svg viewBox="0 0 284 154" preserveAspectRatio="none"><polygon points="0,10 284,0 284,150 0,154" fill="var(--badge-green)"/></svg>
      <div class="claims-leaf" role="img" aria-label="Leaf illustration"></div>
      <ul class="claims-list"><li>0% Additives</li><li>60% Nuts</li><li>100% Natural</li></ul>
    </div>
    <h2 class="flavour-name">Black Forest</h2>
    <p class="ingredients">[ sour cherry and choc ]</p>
    <p class="portion">60g</p>
  </section>

  <section class="wrapper wrapper--plum">
    <div class="seal seal--left"></div><div class="seal seal--right"></div>
    <div class="flavour-texture" role="img" aria-label="Soft dotted pattern hinting at the flavour"></div>
    <div class="brand-tag"><span class="brand-name">NibbleMoss</span></div>
    <div class="claims">
      <svg viewBox="0 0 284 154" preserveAspectRatio="none"><polygon points="0,10 284,0 284,150 0,154" fill="var(--badge-green)"/></svg>
      <div class="claims-leaf" role="img" aria-label="Leaf illustration"></div>
      <ul class="claims-list"><li>0% Additives</li><li>60% Nuts</li><li>100% Natural</li></ul>
    </div>
    <h2 class="flavour-name">Plum Fandango</h2>
    <p class="ingredients">[ banana, apricot and blueberry ]</p>
    <p class="portion">60g</p>
  </section>

  <section class="wrapper wrapper--zest">
    <div class="seal seal--left"></div><div class="seal seal--right"></div>
    <div class="flavour-texture" role="img" aria-label="Soft dotted pattern hinting at the flavour"></div>
    <div class="brand-tag"><span class="brand-name">NibbleMoss</span></div>
    <div class="claims">
      <svg viewBox="0 0 284 154" preserveAspectRatio="none"><polygon points="0,10 284,0 284,150 0,154" fill="var(--badge-green)"/></svg>
      <div class="claims-leaf" role="img" aria-label="Leaf illustration"></div>
      <ul class="claims-list"><li>0% Additives</li><li>60% Nuts</li><li>100% Natural</li></ul>
    </div>
    <h2 class="flavour-name">Zestivelle</h2>
    <p class="ingredients">[ pineapple, passion fruit and kiwi ]</p>
    <p class="portion">60g</p>
  </section>

</main>
</body>
</html>
```